Mortgage Broking boutique Business

I’m wanting a revamped look to my existing business card design. I do like the black and silver but happy to have other colours introduced based on your creation. I’ve attached a copy of my current card so you can have a starting point updated details noted brloe. I deal with high net worth individuals so need my card to be sophisticated, classy that gives off a classy vibe

Target Market(s)

High net worth, wealthy

Industry/Entity Type

Mortgage Brokerage

Contact Information for Business Card

Job title: Finance Executive
Phone: +61 7 3862 1197
Mobile: 0431 275 506
Email: marcus@quillbrookcapital.com.au
Web: www.quillbrookcapital.com.au
Address: level 22 Tamberlin House, 48 Mercer Rd Brisbane QLD 4000

Font styles to use
Other font styles liked:
• Helvetica

Colors

Designer to choose colors to be used in the design.

Requirements
Must have
• Use my existing card design as a starting point

```html
<!DOCTYPE html>
<html lang="en">
<head>
<meta charset="utf-8">
<title>Quillbrook Capital – Business Card</title>
<link href="https://fonts.googleapis.com/css2?family=Jost:wght@400&family=Open+Sans:wght@400;700&display=swap" rel="stylesheet">
<style>
  :root {
    --backdrop: #2e2e30;
    --card-black: #0c0c0c;
    --card-black-soft: #1c1c1c;
    --silver: #c9c9c9;
    --silver-dark: #8e8e8e;
    --paper: #f1f1f1;
    --ink: #141414;
    --accent: #d2d21c;
    --logo-text: #e6e6e6;
  }
  * { margin: 0; padding: 0; box-sizing: border-box; }
  html, body { width: 1200px; height: 782px; overflow: hidden; }
  body { background: var(--backdrop); position: relative; font-family: "Open Sans", Arial, sans-serif; }

  .card {
    position: absolute;
    width: 520px;
    height: 318px;
    box-shadow: 0 14px 30px rgba(0,0,0,.55);
    overflow: hidden;
  }

  /* Front */
  .card-front {
    left: 600px; top: 70px;
    background: radial-gradient(ellipse at center, var(--card-black-soft) 0%, var(--card-black) 75%);
  }
  .frame {
    position: absolute;
    border: 3px solid var(--silver);
    outline: 2px solid var(--silver-dark);
    outline-offset: 4px;
  }
  .card-front .frame { inset: 38px 44px; }
  .brand-name {
    position: absolute;
    font-family: "Jost", "Helvetica Neue", Arial, sans-serif;
    font-weight: 400;
    color: var(--logo-text);
    text-transform: uppercase;
    letter-spacing: .32em;
    line-height: 1.15;
    white-space: nowrap;
  }
  .card-front .brand-name {
    left: 50%; top: 50%;
    transform: translate(-50%, -50%);
    font-size: 27px;
    text-align: left;
  }
  .brand-name .line-two { display: block; padding-left: 1.4em; }

  /* Back */
  .card-back {
    left: 80px; top: 400px;
    background: var(--paper);
  }
  .back-panel {
    position: absolute;
    left: 0; top: 0; bottom: 0;
    width: 178px;
    background: radial-gradient(ellipse at center, var(--card-black-soft) 0%, var(--card-black) 80%);
  }
  .back-panel .frame { inset: 14px 12px 14px 14px; }
  .back-panel .brand-name {
    left: 50%; top: 50%;
    transform: translate(-50%, -50%) rotate(-90deg);
    font-size: 21px;
  }

  .contact {
    position: absolute;
    left: 215px; top: 74px;
    color: var(--ink);
  }
  .person-name {
    font-weight: 700;
    font-size: 21px;
    color: var(--accent);
    text-transform: uppercase;
    letter-spacing: .02em;
    line-height: 1.1;
  }
  .person-title { font-size: 14px; margin-bottom: 6px; }
  .contact-list { list-style: none; font-size: 15px; line-height: 1.28; }
  .contact-list li { display: flex; align-items: center; gap: 8px; }
  .contact-list svg { width: 11px; height: 11px; flex: none; fill: var(--accent); }
  .address { font-size: 15px; line-height: 1.28; margin-top: 2px; }
</style>
</head>
<body>

  <section class="card card-front" aria-label="Card front">
    <div class="frame"></div>
    <div class="brand-name">Quillbrook<span class="line-two">Capital</span></div>
  </section>

  <section class="card card-back" aria-label="Card back">
    <div class="back-panel">
      <div class="frame"></div>
      <div class="brand-name">Quillbrook<span class="line-two">Capital</span></div>
    </div>

    <div class="contact">
      <h1 class="person-name">Marcus Reid</h1>
      <p class="person-title">Finance Executive</p>
      <ul class="contact-list">
        <li>
          <svg viewBox="0 0 12 12" aria-hidden="true"><path d="M1 3h10v2l-2 1v5H3V6L1 5z"/></svg>
          +61 7 3862 1197
        </li>
        <li>
          <svg viewBox="0 0 12 12" aria-hidden="true"><path d="M3 0h6v12H3zM4 1.5v8h4v-8z"/></svg>
          0431 275 506
        </li>
        <li>
          <svg viewBox="0 0 12 12" aria-hidden="true"><path d="M0 2h12v8H0zM1 3l5 3.5L11 3z"/></svg>
          marcus@quillbrookcapital.com.au
        </li>
        <li>
          <svg viewBox="0 0 12 12" aria-hidden="true"><circle cx="6" cy="6" r="6"/></svg>
          www.quillbrookcapital.com.au
        </li>
      </ul>
      <p class="address">level 22 Tamberlin House,<br>48 Mercer Rd Brisbane QLD 4000</p>
    </div>
  </section>

</body>
</html>
```